Visitenkarten-Design für Stillberaterin
Zielgruppe
Ich bin Stillberaterin ZMRPT, d. h. ich berate Mütter bei Stillschwierigkeiten. Meine Zielgruppe sind junge Familien, die sich vorab über das Stillen Ihres Kindes informieren möchten, Stillschwierigkeiten (z. B. Schmerzen, schlechte Gewichtszunahme usw.) haben oder Fragen rund ums Stillen haben (Medikamente, Stillen in besonderen Situationen...). Weiterhin biete ich Kurse für den Beikoststart oder zum Abstillen an.
Aufgabenstellung
Auf meiner Visitenkarte sollte mein Logo sowie alle Kontaktdaten klar und deutlich erkennbar sein. Die Farben sind dem Logo anzupassen. Die Schriftarten, die im Logo verwendet werden sind: Be Bright und Apple Tree

```html
<!DOCTYPE html>
<html lang="de">
<head>
<meta charset="utf-8">
<title>Milchzeit-Nest – Visitenkarte</title>
<link href="https://fonts.googleapis.com/css2?family=Titillium+Web:wght@300;400&family=Dancing+Script:wght@400;500&display=swap" rel="stylesheet">
<style>
  :root {
    --stage: #d0d0d0;
    --pink: #ee5aa2;
    --pink-soft: #f7a3cb;
    --pink-light: #fbd3e6;
    --paper: #f8f8f8;
    --ink: #2b2b2b;
  }
  * { margin: 0; padding: 0; box-sizing: border-box; }
  html, body {
    width: 1073px; height: 1200px; overflow: hidden;
    background: var(--stage);
    font-family: "Titillium Web", Arial, sans-serif;
  }
  .card {
    position: absolute; left: 177px; width: 744px; height: 490px;
    box-shadow: 0 3px 10px rgba(0,0,0,.18);
    overflow: hidden;
  }
  /* Vorderseite */
  .card-front { top: 84px; background: var(--pink); }
  .front-illustration {
    position: absolute; left: 0; top: 0; width: 420px; height: 490px;
    background:
      radial-gradient(ellipse 55% 38% at 42% 72%, var(--pink-soft) 0%, rgba(247,163,203,.35) 60%, rgba(238,90,162,0) 100%),
      radial-gradient(ellipse 45% 55% at 50% 30%, rgba(247,163,203,.55) 0%, rgba(238,90,162,0) 100%);
  }
  .brand {
    position: absolute; left: 360px; top: 212px; width: 370px; text-align: center;
  }
  .brand-name {
    font-weight: 300; font-size: 52px; line-height: 1; color: var(--pink-light);
  }
  .brand-tagline {
    margin-top: 6px; font-weight: 300; font-size: 16px; color: var(--pink-light);
  }
  .front-url {
    position: absolute; left: 420px; top: 514px; width: 310px; text-align: center;
    font-family: "Dancing Script", cursive; font-weight: 400; font-size: 21px; color: var(--pink-light);
  }
  /* Rückseite */
  .card-back { top: 642px; background: var(--paper); }
  .person-name {
    position: absolute; left: 80px; top: 86px;
    font-family: "Dancing Script", cursive; font-weight: 500; font-size: 56px; line-height: 1.2; color: var(--pink);
  }
  .person-role {
    position: absolute; left: 81px; top: 165px;
    font-size: 17px; color: var(--ink);
  }
  .person-role .divider { color: var(--pink); margin: 0 3px; }
  .rule {
    position: absolute; left: 82px; top: 225px; width: 604px; height: 4px; background: var(--pink);
  }
  .address {
    position: absolute; left: 87px; top: 260px; font-style: normal;
    font-size: 22px; line-height: 33px; color: var(--ink);
  }
  .contact-list {
    position: absolute; left: 86px; top: 346px; list-style: none;
  }
  .contact-list li {
    display: flex; align-items: center; height: 32px; font-size: 22px; color: var(--ink);
  }
  .contact-list svg { width: 20px; height: 20px; margin-right: 14px; flex: none; }
</style>
</head>
<body>
  <section class="card card-front">
    <div class="front-illustration" role="img" aria-label="Strichzeichnung einer stillenden Mutter mit Herzform"></div>
    <div class="brand">
      <div class="brand-name">Milchzeit-Nest</div>
      <div class="brand-tagline">Stillberatung für Regensburg</div>
    </div>
    <div class="front-url" style="top:430px">www.milchzeit-nest.de</div>
  </section>

  <section class="card card-back">
    <h1 class="person-name">Lena Hofmeister</h1>
    <p class="person-role">Fachkinderkrankenschwester<span class="divider">|</span>Still- &amp; Laktationsberaterin ZMRPT</p>
    <div class="rule"></div>
    <address class="address">Am Lindenhang 14<br>93080 Pentling</address>
    <ul class="contact-list">
      <li>
        <svg viewBox="0 0 24 24" aria-hidden="true"><path fill="var(--pink)" d="M6.6 10.8a15.1 15.1 0 0 0 6.6 6.6l2.2-2.2a1 1 0 0 1 1-.25 11.4 11.4 0 0 0 3.6.57 1 1 0 0 1 1 1V20a1 1 0 0 1-1 1A17 17 0 0 1 3 4a1 1 0 0 1 1-1h3.5a1 1 0 0 1 1 1c0 1.25.2 2.450.57 3.57a1 1 0 0 1-.25 1z"/></svg>
        09401 2718035
      </li>
      <li>
        <svg viewBox="0 0 24 24" aria-hidden="true"><rect x="2" y="5" width="20" height="14" fill="var(--pink)"/><path d="M2 5l10 8 10-8M2 19l7-6M22 19l-7-6" stroke="var(--paper)" stroke-width="1.5" fill="none"/></svg>
        lena@milchzeit-nest.de
      </li>
      <li>
        <svg viewBox="0 0 24 24" aria-hidden="true" fill="none" stroke="var(--pink)" stroke-width="1.5"><circle cx="12" cy="12" r="9.5"/><ellipse cx="12" cy="12" rx="4.5" ry="9.5"/><path d="M2.5 12h19M4 7h16M4 17h16"/></svg>
        www.milchzeit-nest.de
      </li>
    </ul>
  </section>
</body>
</html>
```